Wordpress website design for a high-end painting business

We are currently rebranding and are looking to update our Wordpress theme. We have recently rebranded our logo on ArtHatchery, and would like our website to be equally as refined.
Our business is named “Holloway Coatings”. We are a high-end painting business that is known for being professional and having high standards. Our clean and professional image is important as it separates us from our competition. Our current website can be found at www.hollowayfinishes.co.nz . We designed the site ourselves so it is understandably rudimentary. We are generally happy with the. page layout of our existing site, but we like a professional remodel. Any ideas on improvement welcomed.
We would like the front page of the website to summarise all of the info throughout the whole website (I.e introduction, photos, testimonials, contact info etc.) as visitors typically scroll through the first page to see that we are reputable and get to our contact number/email contact at the bottom of the page. We would like this first page to give a clean well rounded image of our business. We would like the gallery to be a scroll through of large photos, as it is difficult to see paint details in smaller photos. A contact page with an enquiry section would also be good.
For the colour scheme, we would like something that fits a bold, masculine and high end theme (similar to our logo attached).
We would like the footer to include Velnor paint logos and the accredited painter logo we have included as these are important to our profession.
We have attached some photos of our work also. I will add more in the coming days. More can also be found on our website.
If you have questions or comments, please don’t hesitate to ask and I will get back as soon as possible.
We are open to your own interpretation or ideas for a better layout/site provided they fit the general brief of being a well rounded site for our profession.
Thanks,
Holloway Coatings.
Target Market(s)
High end clients
Industry/Entity Type
Painting (interior and exterior)
Coding
Coded - Design and coding required
Requirements
Must have
- Classy feel, separating us from typical painting companies. Well rounded homepage.
Nice to have
- Lots of examples of our work
Should not have
- Untidy paint motifs (eg, paint droplets, paint splashes)

```html
<!DOCTYPE html>
<html lang="en">
<head>
<meta charset="utf-8">
<title>Holloway Coatings – High-End Painting</title>
<link rel="stylesheet" href="https://fonts.googleapis.com/css2?family=Poppins:wght@400;500;600;700&family=Open+Sans:wght@400;600&display=swap">
<style>
:root{
  --navy:#1d2330;
  --navy-2:#262d3b;
  --bronze:#8b6a3e;
  --bronze-light:#a9844f;
  --cream:#f3ecdc;
  --white:#ffffff;
  --ink:#2a2a2a;
  --muted:#6b6b6b;
  --star:#e2a63b;
}
*{box-sizing:border-box;margin:0;padding:0}
html,body{width:1200px;height:4588px;overflow:hidden}
body{position:relative;background:var(--white);font-family:"Open Sans",sans-serif;color:var(--ink)}
h1,h2,h3,.nav a,.btn{font-family:"Poppins",sans-serif}
section,header,footer{position:absolute;left:0;width:1200px}
.abs{position:absolute}

/* header */
.site-header{top:0;height:180px;background:var(--navy)}
.topbar{position:absolute;left:340px;top:14px;display:flex;gap:26px;color:#d8d8d8;font-size:13px;align-items:center}
.topbar span{display:flex;align-items:center;gap:8px}
.topbar svg{width:14px;height:14px;fill:var(--bronze-light)}
.socials{position:absolute;top:12px;right:100px;display:flex;gap:8px}
.socials i{display:block;width:24px;height:24px;border-radius:50%;background:var(--white)}
.brand{position:absolute;left:40px;top:30px;width:160px;text-align:center;color:var(--white)}
.brand .mark{width:58px;height:58px;border-radius:50%;border:2px solid var(--bronze-light);margin:0 auto 8px}
.brand b{font-family:"Poppins",sans-serif;font-weight:600;font-size:16px;letter-spacing:1px;text-transform:uppercase;display:block}
.nav{position:absolute;left:250px;top:82px;width:860px;display:flex;justify-content:space-between;align-items:center;border-bottom:1px solid #3a4252;padding-bottom:10px}
.nav a{color:var(--white);text-decoration:none;font-size:14px;padding:8px 26px}
.nav a.current{color:var(--bronze-light);border-bottom:2px solid var(--bronze-light)}
.nav a.cta{background:var(--bronze);border-radius:3px}

/* hero */
.hero{top:180px;height:660px;background:linear-gradient(90deg,#f4f4f4 0%,#ececec 50%,#dcdcdc 100%);overflow:hidden}
.hero-photo{position:absolute;right:0;top:0;width:620px;height:660px;background:linear-gradient(160deg,#cfcfcf 0%,#2f3b52 55%,#1f2636 100%)}
.hero-text{position:absolute;left:110px;top:210px}
.hero-text h1{font-size:44px;line-height:1.15;font-weight:700;color:var(--navy)}
.hero-text p{margin-top:12px;font-size:18px;color:var(--ink);padding-left:100px}
.btn{display:inline-block;background:var(--bronze);color:var(--white);font-size:12px;padding:9px 22px;border-radius:20px;text-decoration:none}
.hero-text .btn{margin-top:26px;margin-left:88px}
.drip{position:absolute;left:0;width:1200px}

/* about */
.about{top:840px;height:380px;text-align:center}
.section-title{font-size:40px;font-weight:500;color:var(--ink)}
.section-title em{font-style:normal;color:var(--bronze);font-weight:600}
.rule{width:70px;height:3px;background:var(--bronze);margin:12px auto 0}
.about h3{margin-top:22px;font-size:15px;font-weight:600}
.about p{width:620px;margin:18px auto 0;font-size:13px;line-height:1.7;color:var(--muted)}
.more{display:inline-block;margin-top:22px;font-size:12px;font-weight:600;color:var(--ink)}
.more::before{content:"\2192  "}

/* services */
.services{top:1200px;height:1270px;background:var(--cream);text-align:center}
.services .section-title{margin-top:140px}
.service{position:absolute;width:250px;text-align:center}
.service .pic{width:208px;height:208px;border-radius:50%;margin:0 auto;border:8px solid var(--navy);position:relative}
.service .badge{position:absolute;left:50%;bottom:-20px;width:44px;height:44px;margin-left:-22px;border-radius:50%;background:var(--bronze);border:3px solid var(--cream);display:flex;align-items:center;justify-content:center}
.service .badge svg{width:20px;height:20px;fill:var(--white)}
.service h3{margin-top:36px;font-size:18px;font-weight:600}
.service p{margin-top:8px;font-size:11.5px;line-height:1.6;color:var(--muted)}
.service .more{margin-top:14px}

/* testimonials */
.testimonials{top:2470px;height:620px;text-align:center}
.testimonials .section-title{margin-top:90px}
.quote{position:absolute;width:280px;text-align:center}
.quote p{font-size:11.5px;line-height:1.65;color:var(--muted)}
.quote .who{margin-top:18px;font-size:12px;color:var(--ink)}
.stars{color:var(--star);font-size:18px;letter-spacing:3px;margin-top:4px}
.quote .avatar{width:110px;height:72px;margin:12px auto 0;background:linear-gradient(135deg,#c9b4a0,#5a4a3e)}

/* contact */
.contact{top:3080px;height:820px;background:var(--cream)}
.contact h2{position:absolute;left:0;width:1200px;text-align:center;top:120px;font-size:38px;font-weight:600;line-height:1.25;color:var(--navy)}
.contact h2 em{font-style:normal;color:var(--bronze)}
.contact .rule{position:absolute;left:565px;top:232px;margin:0}
.info{position:absolute;left:170px;display:flex;gap:14px;align-items:flex-start}
.info .ic{width:38px;height:38px;border-radius:50%;border:2px solid var(--navy);display:flex;align-items:center;justify-content:center;flex:none}
.info .ic svg{width:18px;height:18px;fill:var(--navy)}
.info b{font-family:"Poppins",sans-serif;font-size:14px;display:block}
.info span{font-size:13px;color:var(--muted)}
.map{position:absolute;left:170px;top:440px;width:320px;height:280px;background:linear-gradient(135deg,#e4e6e8,#c8ccd1);border:2px solid var(--white)}
.form{position:absolute;left:640px;top:230px;width:350px;height:540px;background:var(--navy);border-radius:8px;border:4px solid #3a4252;padding:26px 22px;z-index:3}
.form label{display:block;color:var(--white);font-size:12px;margin-top:12px}
.form .field{height:32px;background:var(--white);border-radius:2px;margin-top:4px}
.form .field.tall{height:80px}
.form .send{margin-top:18px;height:34px;background:var(--navy-2);border:1px solid #55607a;color:var(--white);font-size:12px;display:flex;align-items:center;justify-content:center;font-family:"Poppins",sans-serif}

/* footer */
.site-footer{top:3880px;height:708px;background:var(--navy);color:var(--white);text-align:center}
.site-footer .brand{position:absolute;left:520px;top:110px}
.foot-nav{position:absolute;top:270px;left:300px;width:600px;display:flex;justify-content:space-between;font-size:13px;font-family:"Poppins",sans-serif}
.foot-nav .current{color:var(--bronze-light)}
.foot-contact{position:absolute;top:304px;left:0;width:1200px;display:flex;justify-content:center;gap:24px;font-size:12px;color:#d8d8d8}
.foot-social{position:absolute;top:336px;left:0;width:1200px;display:flex;justify-content:center;gap:8px}
.foot-social i{width:22px;height:22px;background:var(--bronze);border-radius:3px;display:block}
.sponsor{position:absolute;top:376px;left:0;width:1200px;font-family:"Poppins",sans-serif;font-size:12px;font-weight:600;letter-spacing:1px}
.sponsor-box{position:absolute;top:400px;left:540px;width:120px;height:70px;background:#1c4a9c;display:flex;align-items:center;justify-content:center;font-family:"Poppins",sans-serif;font-weight:700;font-size:22px;color:var(--white)}
.copyright{position:absolute;top:548px;left:0;width:1200px;font-size:12px;color:#cfcfcf}
</style>
</head>
<body>

<header class="site-header">
  <div class="brand"><div class="mark"></div><b>Holloway Coatings</b></div>
  <div class="topbar">
    <span><svg viewBox="0 0 24 24"><path d="M12 2a7 7 0 0 0-7 7c0 5 7 13 7 13s7-8 7-13a7 7 0 0 0-7-7zm0 9.5A2.5 2.5 0 1 1 12 6.5a2.5 2.5 0 0 1 0 5z"/></svg>Kestrel Vale, Waikato</span>
    <span><svg viewBox="0 0 24 24"><path d="M6.6 10.8a15 15 0 0 0 6.6 6.6l2.2-2.2c.3-.3.7-.4 1-.2 1.1.4 2.3.6 3.6.6.6 0 1 .4 1 1V20c0 .6-.4 1-1 1A17 17 0 0 1 3 4c0-.6.4-1 1-1h3.5c.6 0 1 .4 1 1 0 1.3.2 2.5.6 3.6.1.3 0 .7-.2 1z"/></svg>021 555 0148</span>
    <span><svg viewBox="0 0 24 24"><path d="M2 5h20v14H2zm2 2v.5l8 5 8-5V7z"/></svg>hello@hollowaycoatings.co.nz</span>
  </div>
  <div class="socials"><i></i><i></i><i></i></div>
  <nav class="nav">
    <a class="current">Home</a><a>About Us</a><a>Our Services</a><a>Testimony</a><a class="cta">Contact Us</a>
  </nav>
</header>

<section class="hero">
  <div class="hero-photo" role="img" aria-label="Painter in a dark work shirt holding a paint roller"></div>
  <div class="hero-text">
    <h1>Welcome To<br>Holloway Coatings</h1>
    <p>Always On Target</p>
    <a class="btn">Learn More</a>
  </div>
  <svg class="drip" style="bottom:0" height="90" viewBox="0 0 1200 90" preserveAspectRatio="none"><path fill="#fff" d="M0 60 C60 40 90 70 150 50 S260 30 320 55 440 40 500 60 620 35 700 55 820 30 900 50 1020 35 1080 55 1160 40 1200 50 V90 H0Z"/></svg>
</section>

<section class="about">
  <h2 class="section-title">About <em>Holloway Coatings</em></h2>
  <div class="rule"></div>
  <h3>We Take A Lot Of Pride In Our Work</h3>
  <p>Here at Holloway Coatings, we take a lot of pride in our work. We strive to ensure the highest quality paint work, paying close attention to detail to provide a long-lasting finish. Our clients are always our priority; we aim to deliver beyond their expectations. It is our goal to provide an excellent service from start to finish through clear communication, fair pricing and transparency with our pricing.</p>
  <a class="more">Know More</a>
</section>

<section class="services">
  <svg class="drip" style="top:0" height="70" viewBox="0 0 1200 70" preserveAspectRatio="none"><path fill="#fff" d="M0 0 H1200 V30 C1100 60 1000 10 880 40 S640 60 520 30 300 10 180 40 60 50 0 30Z"/></svg>
  <h2 class="section-title">Our <em>Services</em></h2>
  <div class="rule"></div>

  <div class="service" style="left:230px;top:250px">
    <div class="pic" role="img" aria-label="Exterior wall being painted" style="background:linear-gradient(135deg,#7fbfa8,#3f6a8a)"><div class="badge"><svg viewBox="0 0 24 24"><path d="M12 3 2 12h3v8h5v-5h4v5h5v-8h3z"/></svg></div></div>
    <h3>Exterior Painting</h3>
    <p>Lorem ipsum dolor sit amet, consectetur adipiscing elit, sed do eiusmod tempor incididunt ut labore et dolore magna aliqua.</p>
    <a class="more">Know More</a>
  </div>
  <div class="service" style="left:475px;top:250px">
    <div class="pic" role="img" aria-label="Interior wall being rolled with paint" style="background:linear-gradient(135deg,#e8e4de,#9a8f86)"><div class="badge"><svg viewBox="0 0 24 24"><path d="M12 3 2 12h3v8h14v-8h3z"/></svg></div></div>
    <h3>Interior Painting</h3>
    <p>Lorem ipsum dolor sit amet, consectetur adipiscing elit, sed do eiusmod tempor incididunt ut labore et dolore magna aliqua.</p>
    <a class="more">Know More</a>
  </div>
  <div class="service" style="left:720px;top:250px">
    <div class="pic" role="img" aria-label="Wallpaper being hung on a wall" style="background:linear-gradient(135deg,#3d6fb0,#1e3960)"><div class="badge"><svg viewBox="0 0 24 24"><path d="M5 3h14v18H5zm2 2v14h10V5z"/></svg></div></div>
    <h3>Wallpapering</h3>
    <p>Lorem ipsum dolor sit amet, consectetur adipiscing elit, sed do eiusmod tempor incididunt ut labore et dolore magna aliqua.</p>
    <a class="more">Know More</a>
  </div>

  <div class="service" style="left:230px;top:730px">
    <div class="pic" role="img" aria-label="Plaster being applied with a trowel" style="background:linear-gradient(135deg,#efe9e1,#b9aa98)"><div class="badge"><svg viewBox="0 0 24 24"><path d="M3 14 14 3l7 7-11 11H3z"/></svg></div></div>
    <h3>Plastering</h3>
    <p>Lorem ipsum dolor sit amet, consectetur adipiscing elit, sed do eiusmod tempor incididunt ut labore et dolore magna aliqua.</p>
    <a class="more">Know More</a>
  </div>
  <div class="service" style="left:475px;top:730px">
    <div class="pic" role="img" aria-label="Worker cleaning a house floor" style="background:linear-gradient(135deg,#e2ddd4,#8c8378)"><div class="badge"><svg viewBox="0 0 24 24"><path d="M12 2c4 6 6 9 6 12a6 6 0 0 1-12 0c0-3 2-6 6-12z"/></svg></div></div>
    <h3>Waterblasting &amp; House Cleaning</h3>
    <p>Lorem ipsum dolor sit amet, consectetur adipiscing elit, sed do eiusmod tempor incididunt ut labore.</p>
    <a class="more">Know More</a>
  </div>
  <div class="service" style="left:720px;top:730px">
    <div class="pic" role="img" aria-label="House with a freshly painted roof" style="background:linear-gradient(135deg,#cdd8e4,#5e6b7a)"><div class="badge"><svg viewBox="0 0 24 24"><path d="M12 3 1 12h3l8-6 8 6h3z"/></svg></div></div>
    <h3>Roof Painting</h3>
    <p>Lorem ipsum dolor sit amet, consectetur adipiscing elit, sed do eiusmod tempor incididunt ut labore et dolore magna aliqua.</p>
    <a class="more">Know More</a>
  </div>

  <svg class="drip" style="bottom:0" height="80" viewBox="0 0 1200 80" preserveAspectRatio="none"><path fill="#fff" d="M0 40 C120 10 220 60 360 35 S600 10 720 40 960 70 1080 40 1180 30 1200 35 V80 H0Z"/></svg>
</section>

<section class="testimonials">
  <h2 class="section-title">Check What <em>Our Client say</em></h2>
  <div class="rule"></div>
  <div class="quote" style="left:320px;top:210px">
    <p>Lorem ipsum dolor sit amet, consectetur adipiscing elit, sed do eiusmod tempor incididunt ut labore et dolore magna aliqua. Ut enim ad minim veniam, quis nostrud exercitation ullamco laboris nisi ut aliquip ex ea commodo consequat. Duis aute irure dolor in reprehenderit in voluptate velit esse cillum dolore eu fugiat nulla pariatur.</p>
    <div class="who">Mara Quill</div>
    <div class="stars">★★★★★</div>
    <div class="avatar" role="img" aria-label="Photo of a happy client couple"></div>
  </div>
  <div class="quote" style="left:620px;top:210px">
    <p>Lorem ipsum dolor sit amet, consectetur adipiscing elit, sed do eiusmod tempor incididunt ut labore et dolore magna aliqua. Ut enim ad minim veniam, quis nostrud exercitation ullamco laboris nisi ut aliquip ex ea commodo consequat. Duis aute irure dolor in reprehenderit in voluptate velit esse cillum dolore eu fugiat nulla pariatur.</p>
    <div class="who">Tom Everly</div>
    <div class="stars">★★★★★</div>
    <div class="avatar" role="img" aria-label="Photo of a satisfied client" style="background:linear-gradient(135deg,#9fb6cc,#36465a)"></div>
  </div>
</section>

<section class="contact">
  <svg class="drip" style="top:0" height="80" viewBox="0 0 1200 80" preserveAspectRatio="none"><path fill="#fff" d="M0 0 H1200 V20 C1150 60 1120 20 1080 30 S1000 70 960 25 880 50 820 20 740 60 700 25 600 45 540 20 460 60 420 25 320 55 260 20 180 50 120 25 40 55 0 20Z"/></svg>
  <h2>Get In<br><em>Touch With Us</em></h2>
  <div class="rule"></div>
  <div class="info" style="top:250px"><div class="ic"><svg viewBox="0 0 24 24"><path d="M6.6 10.8a15 15 0 0 0 6.6 6.6l2.2-2.2c.3-.3.7-.4 1-.2 1.1.4 2.3.6 3.6.6.6 0 1 .4 1 1V20c0 .6-.4 1-1 1A17 17 0 0 1 3 4c0-.6.4-1 1-1h3.5c.6 0 1 .4 1 1 0 1.3.2 2.5.6 3.6.1.3 0 .7-.2 1z"/></svg></div><div><b>Phone</b><span>021 555 0148</span></div></div>
  <div class="info" style="top:315px"><div class="ic"><svg viewBox="0 0 24 24"><path d="M2 5h20v14H2zm2 2v.5l8 5 8-5V7z"/></svg></div><div><b>Email</b><span>hello@hollowaycoatings.co.nz</span></div></div>
  <div class="info" style="top:380px"><div class="ic"><svg viewBox="0 0 24 24"><path d="M12 2a7 7 0 0 0-7 7c0 5 7 13 7 13s7-8 7-13a7 7 0 0 0-7-7zm0 9.5A2.5 2.5 0 1 1 12 6.5a2.5 2.5 0 0 1 0 5z"/></svg></div><div><b>Address</b><span>Kestrel Vale, Waikato</span></div></div>
  <div class="map" role="img" aria-label="Map showing the business location"></div>
  <div class="form">
    <label>Name</label><div class="field"></div>
    <label>Email</label><div class="field"></div>
    <label>Phone</label><div class="field"></div>
    <label>Message</label><div class="field tall"></div>
    <div class="send">&#10148;&nbsp; Send Your Message</div>
  </div>
</section>

<footer class="site-footer">
  <svg class="drip" style="top:-40px" height="80" viewBox="0 0 1200 80" preserveAspectRatio="none"><path fill="#1d2330" d="M0 40 C40 10 80 70 120 40 S200 10 260 45 340 15 400 40 480 70 540 40 620 10 680 45 760 15 820 40 900 70 960 40 1040 10 1100 45 1170 20 1200 40 V80 H0Z"/></svg>
  <div class="brand"><div class="mark"></div><b>Holloway Coatings</b></div>
  <div class="foot-nav"><span class="current">Home</span><span>About Us</span><span>Our Services</span><span>Testimony</span><span>Contact Us</span></div>
  <div class="foot-contact"><span>Kestrel Vale, Waikato</span><span>021 555 0148</span><span>hello@hollowaycoatings.co.nz</span></div>
  <div class="foot-social"><i></i><i></i><i></i></div>
  <div class="sponsor">PRODUCT SPONSORED BY</div>
  <div class="sponsor-box">Velnor</div>
  <div class="copyright">Copyright © 2023 Holloway Coatings Powered By Holloway Coatings</div>
</footer>

</body>
</html>
```